WP website design (Wrexfordale)

We need a wordpress design for an established auction and real estate company based in Viginia- "The Name That Closes!". The winning design will incorporate a professional color scheme with company logo in a clean layout. The design needs to consider that this will be developed on a responsive theme.
Industry/Entity Type
Real Estate
Requirements
Must have
- - - We will require winning designer to provide a layered PSD (Adobe photoshop) concept file, along with any non-standard font files used.
- Logo attached. Color scheme should compliment the logo colors; nothing flashy, rather more business oriented … subdued colors. Lighten up the burgundy color; not so dark on the background;
- Horizontal Navigation menu with these pages:
- Home - Upcoming Auctions - Appraisals - Past Auctions - Real Estate for Sale Sellers - Buyers - About Wrexfordale - Contact Us
- A slideshow element on the home page use stock of real estate for the initial image.
- Sidebar widgets to be included are: Email sign-up form - Featured Auctions - Testimonial widget - 'Our Videos' widget; Social media icons somewhere in layout (facebook, twitter, RSS, and Youtube, linkedIn), News & Events widget, "Special announcements" blog.
- Homepage content is text:
- Wrexfordale is "The name that closes!"
- Wrexfordale Auctioneers International is a premier, full service Auction Company specializing in the sale of commercial and residential real estate through the auction method. In the last 53 years, we have conducted thousands of auctions across the United States and several foreign countries.
- We bring our years of experience in auctioning homes, land, condominiums, industrial properties, retail buildings and development sites to help private individuals, corporations and financial institutions sell their property. In addition, we can assist you with liquidating estates, antiques, equipment and firearms collections.
- We have conducted thousands of auctions, assisting a wide range of companies both large and small achieve maximum value for their capital assets.
Nice to have
- Site will have drop down menus, please show what one will look like.
Should not have
- no gavels should be used in the design

```html
<!DOCTYPE html>
<html lang="en">
<head>
<meta charset="utf-8">
<title>Wrexfordale Auctioneers International</title>
<link rel="stylesheet" href="https://fonts.googleapis.com/css2?family=Arimo:wght@400;700&family=Tinos:wght@400;700&display=swap">
<style>
:root{
  --navy:#2b3467;
  --navy-dark:#232a55;
  --red:#c0312f;
  --red-text:#c8262b;
  --ink:#333333;
  --muted:#555555;
  --rule:#dddddd;
  --white:#ffffff;
  --tweet-head:#55c6ea;
  --tweet-body:#d9d9d9;
}
*{box-sizing:border-box;margin:0;padding:0}
html,body{width:1200px;height:2697px;overflow:hidden}
body{position:relative;background:var(--white);font-family:"Arimo",Arial,sans-serif;color:var(--ink)}
.abs{position:absolute}

/* header */
.site-header{position:absolute;left:0;top:0;width:1200px;height:125px;background:var(--white)}
.brand{position:absolute;left:110px;top:30px;display:flex;align-items:center;gap:10px}
.brand-square{width:22px;height:22px;background:var(--navy)}
.brand-name{font-family:"Arimo",Arial,sans-serif;font-weight:700;font-size:24px;color:var(--navy);line-height:1}
.brand-tag{position:absolute;left:110px;top:68px;font-size:11px;color:var(--ink)}
.partner{position:absolute;left:110px;top:88px;font-size:11px;color:var(--ink);display:flex;align-items:center;gap:6px}
.partner-badge{width:26px;height:12px;background:var(--navy)}
.social{position:absolute;right:80px;top:12px;display:flex;gap:8px}
.social span{width:32px;height:32px;border-radius:50%;background:var(--navy)}
.phone{position:absolute;right:78px;top:60px;display:flex;align-items:center;gap:8px;font-size:29px;font-weight:700;color:var(--red-text)}

/* nav */
.main-nav{position:absolute;left:0;top:125px;width:1200px;height:51px;background:var(--navy)}
.main-nav ul{list-style:none;display:flex;justify-content:space-between;padding:0 78px 0 77px;height:51px;align-items:center}
.main-nav li{font-size:15px;color:var(--white);padding:8px 9px}
.main-nav li.active{background:var(--white);color:var(--red-text);height:51px;padding:17px 14px 0;margin-top:8px}
.dropdown{position:absolute;left:283px;top:176px;width:184px;background:var(--white);list-style:none;padding:6px 12px;box-shadow:0 2px 6px rgba(0,0,0,.25);z-index:3}
.dropdown li{font-size:13px;color:var(--navy);padding:10px 0 9px;border-bottom:1px solid var(--rule)}
.dropdown li:last-child{border-bottom:none}
.dropdown li.current{color:var(--red-text)}

/* hero */
.hero{position:absolute;left:0;top:176px;width:1200px;height:587px;background:linear-gradient(180deg,#5a7fb0 0%,#8aa6c6 22%,#a89a86 45%,#8b7a66 68%,#6f7a4e 86%,#56663a 100%)}
.hero-shade{position:absolute;inset:0;background:rgba(0,0,0,.18)}
.hero-title{position:absolute;left:0;width:1200px;top:180px;text-align:center;color:var(--white);font-family:"Tinos",serif;font-weight:700;font-size:64px;letter-spacing:1px;line-height:1}
.hero-sub{position:absolute;left:0;width:1200px;top:246px;text-align:center;color:var(--white);font-size:25px;letter-spacing:1px}
.hero-text{position:absolute;left:290px;width:620px;top:290px;text-align:center;color:var(--white);font-size:14.5px;line-height:20px}
.hero-dots{position:absolute;left:565px;top:376px;display:flex;gap:10px}
.hero-dots span{width:17px;height:17px;border-radius:50%;background:var(--white)}
.hero-dots span.on{background:#f2c21b}
.hero-down{position:absolute;left:568px;top:495px}

/* features */
.features{position:absolute;left:0;top:763px;width:1200px;height:520px}
.feature{position:absolute;top:62px;width:316px;text-align:center}
.feature h3{font-family:"Tinos",serif;font-weight:700;font-size:24px;color:var(--red-text);letter-spacing:.5px}
.feature .kicker{font-size:13.5px;color:var(--navy);margin-top:4px}
.feature .photo{width:316px;height:204px;margin-top:6px}
.feature p{font-size:12.5px;color:var(--muted);line-height:16px;margin:10px 10px 0}
.btn{display:inline-block;width:112px;height:36px;line-height:36px;border-radius:3px;color:var(--white);font-size:13px;text-align:center}
.btn-navy{background:var(--navy)}
.btn-red{background:var(--red)}
.feature .btn{margin-top:20px}

/* red band */
.intro{position:absolute;left:0;top:1283px;width:1200px;height:405px;background:var(--red);color:var(--white)}
.intro h2{position:absolute;left:78px;top:52px;font-family:"Tinos",serif;font-weight:700;font-size:38px;letter-spacing:.5px}
.intro .lead{position:absolute;left:78px;top:96px;font-family:"Tinos",serif;font-weight:700;font-size:20px}
.intro .body{position:absolute;left:78px;top:138px;width:610px;font-size:12.5px;line-height:19px}
.intro .body p+p{margin-top:17px}
.video{position:absolute;left:735px;top:57px;width:388px;height:302px;background:#000}
.video .vtitle{position:absolute;left:10px;top:8px;font-size:11px;color:#ddd}
.video .play{position:absolute;left:170px;top:118px}
.video .bar{position:absolute;left:0;bottom:0;width:388px;height:26px;background:#1b1b1b}
.video .track{position:absolute;left:0;bottom:26px;width:388px;height:3px;background:#555}
.video .time{position:absolute;left:70px;bottom:7px;font-size:10px;color:#ccc}

/* lower columns */
.lower{position:absolute;left:0;top:1688px;width:1200px;height:525px}
.col-title{font-family:"Tinos",serif;font-size:34px;color:var(--navy)}
.news{position:absolute;left:80px;top:44px;width:305px}
.news-item{margin-top:12px;padding-bottom:14px;border-bottom:1px solid var(--rule)}
.news-item:last-of-type{border-bottom:none}
.item-title{font-size:12px;font-weight:700;color:var(--red-text);white-space:nowrap;letter-spacing:-.2px}
.item-date{font-size:11px;font-weight:700;color:var(--ink);margin-top:2px}
.item-text{font-size:11.5px;color:var(--muted);line-height:15px;margin-top:4px}
.divider{position:absolute;top:44px;width:1px;height:416px;background:var(--rule)}
.testimonials{position:absolute;left:450px;top:44px;width:302px}
.quote{margin-top:12px;padding-bottom:16px;border-bottom:1px solid var(--rule)}
.quote:last-of-type{border-bottom:none}
.quote p{font-size:11.5px;color:var(--muted);line-height:15px}
.quote .by{font-size:12px;font-weight:700;color:var(--red-text);margin-top:8px}
.tweets{position:absolute;left:805px;top:44px;width:318px;height:410px;background:var(--tweet-body);border:1px solid #c8c8c8}
.tweets-head{height:38px;background:var(--tweet-head);color:var(--white);font-family:"Tinos",serif;font-size:24px;padding:4px 10px}
.tweet{display:flex;gap:10px;margin:0 18px 0 8px;padding:10px 0 9px;border-bottom:1px solid #c4c4c4}
.tweet .avatar{flex:0 0 62px;height:62px;border-radius:50%;background:var(--navy);border:4px solid var(--white)}
.tweet .item-text{margin-top:2px}
.scroll{position:absolute;right:4px;top:46px;width:6px;height:350px;background:#eeeeee;border-radius:3px}
.scroll span{display:block;width:6px;height:40px;background:var(--tweet-head);border-radius:3px}

/* map */
.map{position:absolute;left:0;top:2213px;width:1200px;height:425px;background:linear-gradient(160deg,#ece7dd 0%,#e6e1d6 30%,#a9c4e6 45%,#a3bfe3 100%)}
.contact-card{position:absolute;left:438px;top:2345px;width:324px;height:220px;background:var(--red);color:var(--white);text-align:center;padding-top:26px}
.contact-card .co{font-size:13px;line-height:17px}
.contact-card .lines{font-size:15px;line-height:22px;margin-top:20px}
.to-top{position:absolute;left:1133px;top:2522px;width:50px;height:50px;background:var(--white);border:1px solid #ccc}

/* footer */
.site-footer{position:absolute;left:0;top:2638px;width:1200px;height:59px;background:var(--navy);color:var(--white);text-align:center;font-size:10.5px;line-height:15px;padding-top:15px}
</style>
</head>
<body>

<header class="site-header">
  <div class="brand">
    <span class="brand-square"></span>
    <span class="brand-name">Wrexfordale Auctioneers International</span>
  </div>
  <div class="brand-tag">"The Name That Closes!"</div>
  <div class="partner">an alliance partner of <span class="partner-badge"></span> Norland Partners</div>
  <div class="social"><span></span><span></span><span></span><span></span></div>
  <div class="phone">
    <svg width="28" height="28" viewBox="0 0 24 24" aria-hidden="true"><path fill="#c8262b" d="M6.6 10.8c1.4 2.8 3.8 5.1 6.6 6.6l2.2-2.2c.3-.3.7-.4 1-.2 1.1.4 2.3.6 3.6.6.6 0 1 .4 1 1V20c0 .6-.4 1-1 1C10.6 21 3 13.4 3 4c0-.6.4-1 1-1h3.5c.6 0 1 .4 1 1 0 1.3.2 2.5.6 3.6.1.3 0 .7-.2 1z"/></svg>
    800-555-0147
  </div>
</header>

<nav class="main-nav">
  <ul>
    <li>Home</li>
    <li>Auction Calender</li>
    <li class="active">Auctions</li>
    <li>Real Estate For Sale</li>
    <li>Past Auctions</li>
    <li>About Us</li>
    <li>Auction FAQ</li>
    <li>News and Events</li>
    <li>Contact Us</li>
  </ul>
</nav>
<ul class="dropdown">
  <li>Real Estate Auctions</li>
  <li class="current">Personal Property Auctions</li>
  <li>Charity Auctions</li>
  <li>Online Auctions</li>
</ul>

<section class="hero">
  <div class="abs" style="inset:0" role="img" aria-label="Photo of a large two-storey stucco house with a tiled roof, garage and front lawn"></div>
  <div class="hero-shade"></div>
  <h1 class="hero-title">LOREM IPSUM DOLOR</h1>
  <div class="hero-sub">CONSECTETUR ADIPISCING ELIT</div>
  <p class="hero-text">Lorem ipsum dolor sit amet, consectetur adipiscing elit. Nulla lobortis consequat mauris, eget eleifend nunc viverra viverra. Ut ac risus odio. Aliquam pretium purus sed nulla feugiat blandit. Cras vel libero ut lacus eleifend tempor. Phasellus eleifend,</p>
  <div class="hero-dots"><span></span><span class="on"></span><span></span></div>
  <svg class="hero-down" width="64" height="64" viewBox="0 0 64 64" aria-hidden="true"><circle cx="32" cy="32" r="29" fill="none" stroke="#fff" stroke-width="3"/><path d="M20 27l12 12 12-12" fill="none" stroke="#fff" stroke-width="3.5" stroke-linecap="round" stroke-linejoin="round"/></svg>
</section>

<section class="features">
  <article class="feature" style="left:78px">
    <h3>CRAS VEL LIBERO UT</h3>
    <div class="kicker">Tristique senectus et netus et malesuada fames</div>
    <div class="photo" role="img" aria-label="Photo of a peach two-storey family house with a double garage" style="background:linear-gradient(180deg,#3f7fd6 0%,#7fb0e8 35%,#e3c79e 60%,#b5976f 80%,#5f8f3e 100%)"></div>
    <p>Phasellus mollis pharetra dignissim. Ut pretium blandit lectus congue fringilla. Aliquam imperdiet ante quis odio congue ultrices. Donec at nisl augue, sit amet ultricies leo. Cras viverra lacinia magna, auctor convallis sapien interdum at</p>
    <span class="btn btn-navy">Read More</span>
  </article>
  <article class="feature" style="left:442px">
    <h3>CRAS VEL LIBERO UT</h3>
    <div class="kicker">Tristique senectus et netus et malesuada fames</div>
    <div class="photo" role="img" aria-label="Photo of a white Spanish-style villa with arched windows" style="background:linear-gradient(180deg,#2f6fd0 0%,#6ea2e4 35%,#f1f1ee 58%,#d8d6d0 78%,#6a8a4a 100%)"></div>
    <p>Phasellus mollis pharetra dignissim. Ut pretium blandit lectus congue fringilla. Aliquam imperdiet ante quis odio congue ultrices. Donec at nisl augue, sit amet ultricies leo. Cras viverra lacinia magna, auctor convallis sapien interdum at</p>
    <span class="btn btn-red">Read More</span>
  </article>
  <article class="feature" style="left:806px">
    <h3>CRAS VEL LIBERO UT</h3>
    <div class="kicker">Tristique senectus et netus et malesuada fames</div>
    <div class="photo" role="img" aria-label="Photo of a cream suburban house with a driveway and green lawn" style="background:linear-gradient(180deg,#4a86d8 0%,#8fb9ea 35%,#e7dcc6 58%,#b9ad96 76%,#4f8a35 100%)"></div>
    <p>Phasellus mollis pharetra dignissim. Ut pretium blandit lectus congue fringilla. Aliquam imperdiet ante quis odio congue ultrices. Donec at nisl augue, sit amet ultricies leo. Cras viverra lacinia magna, auctor convallis sapien interdum at</p>
    <span class="btn btn-red">Read More</span>
  </article>
</section>

<section class="intro">
  <h2>DONEC A LECTUS NON</h2>
  <div class="lead">consectetur adipiscing elit. Nulla lobortis consequat</div>
  <div class="body">
    <p>Lorem ipsum dolor sit amet, consectetur adipiscing elit. Nulla lobortis consequat mauris, eget eleifend nunc viverra viverra. Ut ac risus odio. Aliquam pretium purus sed nulla feugiat blandit. Cras vel libero ut lacus eleifend tempor. Phasellus eleifend, magna non tincidunt accumsan, justo arcu cursus ipsum, non porttitor sapien quam vel magna. Maecenas elit nisi, molestie nec dapibus nec, aliquet a erat. Donec scelerisque lacus a libero suscipit auctor volutpat enim euismod. Mauris porta, lacus ut ullamcorper sodales, mauris tortor feugiat purus, nec aliquam neque purus ac metus. Nunc eleifend leo quis nisl hendrerit ultrices. Suspendisse quis feugiat elit. Fusce vitae dolor ac est tincidunt feugiat. Phasellus volutpat dui in sapien.</p>
    <p>Donec a lectus non purus ultricies eleifend. Duis nec augue eget lorem vestibulum suscipit. Integer eget ligula lectus, eget pulvinar diam. Donec porttitor viverra nibh ac pulvinar.</p>
  </div>
  <div class="video">
    <div class="vtitle">Wrexfordale Auctioneers.mov</div>
    <svg class="play" width="48" height="48" viewBox="0 0 48 48" aria-hidden="true"><circle cx="24" cy="24" r="22" fill="#444"/><path d="M19 15l14 9-14 9z" fill="#fff"/></svg>
    <div class="track"></div>
    <div class="bar">
      <svg class="abs" style="left:14px;top:7px" width="12" height="12" viewBox="0 0 12 12" aria-hidden="true"><path d="M1 0l10 6-10 6z" fill="#ccc"/></svg>
    </div>
    <div class="time">0:00 / 0:31</div>
  </div>
</section>

<section class="lower">
  <div class="news">
    <h2 class="col-title">News &amp; Events</h2>
    <div class="news-item">
      <div class="item-title">Lorem ipsum dolor sit amet, consectetur adipiscing</div>
      <div class="item-date">2013-10-09</div>
      <div class="item-text">Integer eget ligula lectus, eget pulvinar diam. Donec porttitor viverra nibh ac pulvinar. Pellentesque habitant morbi tristique senectus et netus et.</div>
    </div>
    <div class="news-item">
      <div class="item-title">Lorem ipsum dolor sit amet, consectetur</div>
      <div class="item-date">2013-10-09</div>
      <div class="item-text">Integer eget ligula lectus, eget pulvinar diam. Donec porttitor viverra nibh ac pulvinar. Pellentesque habitant morbi tristique senectus et netus et.</div>
    </div>
    <div class="news-item">
      <div class="item-title">Lorem ipsum dolor sit amet, consectetur adipiscing elit.</div>
      <div class="item-date">2013-10-09</div>
      <div class="item-text">Integer eget ligula lectus, eget pulvinar diam. Donec porttitor viverra nibh ac pulvinar. Pellentesque habitant morbi tristique senectus et netus et.</div>
    </div>
    <span class="btn btn-navy" style="margin-top:4px">Read More</span>
  </div>
  <div class="divider" style="left:415px"></div>

  <div class="testimonials">
    <h2 class="col-title">Testimonials</h2>
    <div class="quote">
      <p>"Integer eget ligula lectus, eget pulvinar diam. Donec porttitor viverra nibh ac pulvinar. Pellentesque habitant morbi tristique senectus et netus et. Pellentesque habitant morbi tristique senectus et netus et."</p>
      <div class="by">Lorem ipsum dolor</div>
    </div>
    <div class="quote">
      <p>"Integer eget ligula lectus, eget pulvinar diam. Donec porttitor viverra nibh ac pulvinar. Pellentesque habitant morbi tristique senectus et netus et. Pellentesque habitant morbi tristique senectus"</p>
      <div class="by">Lorem ipsum</div>
    </div>
    <div class="quote">
      <p>"Integer eget ligula lectus, eget pulvinar diam. Donec porttitor viverra nibh ac pulvinar. Pellentesque habitant morbi tristique senectus et netus et. Pellentesque habitant morbi tristique senectus et netus et."</p>
      <div class="by">Lorem ipsum dolor sit</div>
    </div>
    <span class="btn btn-red" style="margin-top:4px">Read More</span>
  </div>
  <div class="divider" style="left:780px"></div>

  <aside class="tweets">
    <div class="tweets-head">Latest Tweets</div>
    <div class="tweet"><span class="avatar"></span><div><div class="item-title">Lorem ipsum dolor sit amet,</div><div class="item-date">2013-10-09</div><div class="item-text">Integer eget ligula lectus, eget pulvinar diam. Donec porttitor viverra nibh ac pulvinar. Pellentesque habitant</div></div></div>
    <div class="tweet"><span class="avatar"></span><div><div class="item-title">Lorem ipsum dolor sit amet,</div><div class="item-date">2013-10-09</div><div class="item-text">Integer eget ligula lectus, eget pulvinar diam. Donec porttitor</div></div></div>
    <div class="tweet"><span class="avatar"></span><div><div class="item-title">Lorem ipsum dolor sit amet,</div><div class="item-date">2013-10-09</div><div class="item-text">Integer eget ligula lectus, eget pulvinar diam. Donec porttitor viverra nibh ac</div></div></div>
    <div class="tweet" style="border-bottom:none"><span class="avatar"></span><div><div class="item-title">Lorem ipsum dolor sit amet,</div><div class="item-date">2013-10-09</div><div class="item-text">Integer eget ligula lectus, eget pulvinar diam. Donec porttitor viverra nibh</div></div></div>
    <div class="scroll"><span></span></div>
  </aside>
</section>

<div class="map" role="img" aria-label="Street map showing the office location beside a lake, with a red location pin"></div>
<div class="contact-card">
  <div class="co">Wrexfordale Auctioneers International, LTD, Inc.<br>2417 Crestmoor Square, Fairhaven, VA. 24599</div>
  <div class="lines">Email: auction@wrexfordale-auctions.com<br>Toll Free: 1-800-555-0147<br>Phone: 540-555-0192</div>
</div>
<div class="to-top">
  <svg width="48" height="48" viewBox="0 0 48 48" aria-hidden="true"><path d="M14 29l10-10 10 10" fill="none" stroke="#c0312f" stroke-width="3" stroke-linecap="round" stroke-linejoin="round"/></svg>
</div>

<footer class="site-footer">
  Copyright © 2010 - 2013 • All Rights Reserved • Wrexfordale Auctioneers International, LTD, Inc.<br>
  Powered by: BidWorksHub.com and GavelPointListings.com
</footer>

</body>
</html>
```